Letterhead and compliment slip

We are a UK-based market research agency. We are looking for a new letterhead design to incorporate our logo, address details and company information. We are looking for a simple design. It should be modern. It needs to have a qualify feel. As we are UK based it needs to be designed for A4 paper size (letterhead).
I'm really looking for something simple in design terms!
Both letterhead and compliment slip need to include:
Our logo
Company address
Telephone number
Email address
Website address
Company registration number
VAT registration number
Grey and green would be a good colour scheme to fit with our logo

```html
<!DOCTYPE html>
<html lang="en">
<head>
<meta charset="utf-8">
<title>Meridian Research – Letterhead</title>
<link rel="stylesheet" href="https://fonts.googleapis.com/css2?family=Roboto:wght@400;700&family=Open+Sans:wght@400&display=swap">
<style>
  :root {
    --brand-green: #a6cf38;
    --text-grey: #8c8c8c;
    --ink-grey: #6f6f6f;
    --paper: #ffffff;
    --grid-tint: #f7f8f3;
    --backdrop: #ececec;
  }
  * { margin: 0; padding: 0; box-sizing: border-box; }
  html, body { width: 1200px; height: 1000px; overflow: hidden; }
  body { background: var(--backdrop); font-family: "Open Sans", Arial, sans-serif; position: relative; }

  .letterhead { position: absolute; left: 303px; top: 28px; width: 594px; height: 840px; background: var(--paper); box-shadow: 0 6px 18px rgba(0,0,0,.12); }
  .letterhead__art { position: absolute; inset: 0; }

  .brand { position: absolute; right: 26px; top: 18px; display: flex; align-items: center; gap: 8px; }
  .brand__dot { width: 18px; height: 18px; border-radius: 50%; background: var(--brand-green); }
  .brand__name { font-family: "Roboto", Arial, sans-serif; font-weight: 700; font-size: 30px; color: var(--brand-green); letter-spacing: -0.5px; }

  .company-details { position: absolute; left: 22px; top: 738px; font-size: 6.6px; line-height: 9.6px; color: var(--ink-grey); }

  .mini-contacts { position: absolute; right: 22px; top: 812px; display: flex; gap: 12px; font-size: 6.5px; color: var(--ink-grey); align-items: center; }
  .mini-contacts span { display: flex; align-items: center; gap: 4px; }
  .mini-contacts svg { width: 9px; height: 9px; fill: var(--text-grey); }

  .contact-bar { position: absolute; left: 368px; top: 888px; display: flex; gap: 26px; align-items: center; font-size: 17px; color: var(--text-grey); }
  .contact-bar__item { display: flex; align-items: center; gap: 9px; }
  .contact-bar__item svg { height: 28px; fill: var(--text-grey); }
</style>
</head>
<body>

<section class="letterhead" aria-label="A4 letterhead">
  <svg class="letterhead__art" viewBox="0 0 594 840" width="594" height="840">
    <path class="letterhead__writing-area" role="img" aria-label="Dotted writing grid"
          d="M8 56 C120 34 200 42 300 64 S500 96 586 96 L586 738 C520 744 440 742 350 730 S150 705 8 716 Z"
          fill="var(--grid-tint)"/>
    <path d="M0 52 C120 30 200 38 300 60 S500 92 594 92" fill="none" stroke="var(--brand-green)" stroke-width="7"/>
    <path d="M0 720 C150 709 250 712 350 734 S520 748 594 742" fill="none" stroke="var(--brand-green)" stroke-width="7"/>
    <rect x="4" y="4" width="586" height="832" fill="none" stroke="var(--brand-green)" stroke-width="8"/>
  </svg>

  <div class="brand">
    <span class="brand__dot"></span>
    <span class="brand__name">Meridian Research</span>
  </div>

  <address class="company-details" style="font-style:normal">
    Meridian Research Ltd<br>
    12 Abbey Court<br>
    Harlow Road<br>
    St Albans<br>
    Hertfordshire<br>
    AL1 4XZ<br>
    Company registration number: 08123456<br>
    VAT registration number: 912 3456 78
  </address>

  <div class="mini-contacts">
    <span><svg viewBox="0 0 24 24"><path d="M6.6 10.8a15 15 0 006.6 6.6l2.2-2.2c.3-.3.7-.4 1-.2 1.1.4 2.3.6 3.6.6.6 0 1 .4 1 1V20c0 .6-.4 1-1 1C10.6 21 3 13.4 3 4c0-.6.4-1 1-1h3.5c.6 0 1 .4 1 1 0 1.3.2 2.5.6 3.6.1.3 0 .7-.2 1z"/></svg>+44 (0)1632 960418</span>
    <span><svg viewBox="0 0 24 24"><circle cx="12" cy="12" r="10"/></svg>www.meridianresearch.co.uk</span>
    <span><svg viewBox="0 0 24 24"><path d="M2 5h20v14H2z"/></svg>info@meridianresearch.co.uk</span>
  </div>
</section>

<div class="contact-bar">
  <div class="contact-bar__item">
    <svg viewBox="0 0 24 24" width="28"><path d="M6.6 10.8a15 15 0 006.6 6.6l2.2-2.2c.3-.3.7-.4 1-.2 1.1.4 2.3.6 3.6.6.6 0 1 .4 1 1V20c0 .6-.4 1-1 1C10.6 21 3 13.4 3 4c0-.6.4-1 1-1h3.5c.6 0 1 .4 1 1 0 1.3.2 2.5.6 3.6.1.3 0 .7-.2 1z"/></svg>
    <span>+44 (0)1632 960418</span>
  </div>
  <div class="contact-bar__item">
    <svg viewBox="0 0 24 24" width="38" style="fill:none;stroke:var(--text-grey);stroke-width:1.4"><circle cx="12" cy="12" r="10.5"/><ellipse cx="12" cy="12" rx="4.5" ry="10.5"/><path d="M1.5 12h21M3 7h18M3 17h18"/></svg>
    <span>www.meridianresearch.co.uk</span>
  </div>
  <div class="contact-bar__item">
    <svg viewBox="0 0 32 22" width="40"><rect width="32" height="22"/><path d="M1 1l15 11L31 1" fill="none" stroke="#fff" stroke-width="1.5"/></svg>
    <span>info@meridianresearch.co.uk</span>
  </div>
</div>

</body>
</html>
```